Graphic Design for Labels

I'm needing a label for my skincare line based in Cedar Bay, BC. The name of the company is 'Linden Mist Skincare' and the tag line is 'Stay Gentle with Your Face'. It should indicate somewhere on the lable that it is made with raw fireweed honey.
There are two products the first is Moisturizing Face Cream and second is Nourishing Face Buff. I would like some honey-comb incorporated around the edges of the label and a black and white detailed honeybee somewhere on the label, maybe looking like it was hand drawn with a fine tip black marker or pencil. It will need to have the amount of product in the front which is 120 ml.
I'm open to different colours but nothing too bright, I want a delicate feel to the colours. Overall I would like the label to have a boutiquey artisan feel. I will also require an ingredient label for the back of the bottles the exact same size as the front label with the company info there as well. And some directions. The ingredients and directions can read whatever for now and I will provide those details when I'm ready to order the labels if that's possible, if not let me know asap and I can provide the details. After the ingredients list I would like it to read:
'Paraben and Sulfate free'
At the bottom of the back label I would like it to read:
'Please Recycle'
and then the company name and location at the very bottom
Updates
I like the way this label is organized, and especially how the company name is in the circle around the butterfly. Maybe that could be done with a honey bee and if the Net Weight could be included like it is on this bottle that would be great - 4 oz (115g)
The flowers are nice, but maybe it would look good to have simlpe hand drawn flowers with a bee flying around, if possible?
Target Market(s)
Women
Industry/Entity Type
Graphic Design
Look and feel
Each slider illustrates characteristics of the customer's brand and the style your logo design should communicate.

```html
<!DOCTYPE html>
<html lang="en">
<head>
<meta charset="utf-8">
<title>Linden Mist Skincare – Label Front and Back</title>
<link href="https://fonts.googleapis.com/css2?family=Questrial&family=Gochi+Hand&display=swap" rel="stylesheet">
<style>
  :root {
    --page: #ffffff;
    --frame: #b5b5b5;
    --honey: #f7be25;
    --honey-pale: #fdeec4;
    --ink: #111111;
    --muted: #555555;
  }
  * { margin: 0; padding: 0; box-sizing: border-box; }
  html, body { width: 1200px; height: 1001px; overflow: hidden; background: var(--page); }
  body { position: relative; font-family: "Questrial", sans-serif; color: var(--ink); }

  .label {
    position: absolute; top: 136px; width: 398px; height: 644px;
    border: 2px solid var(--frame); background: var(--page); overflow: hidden;
  }
  .label--front { left: 188px; }
  .label--back { left: 621px; }

  .caption {
    position: absolute; top: 824px; width: 200px; text-align: center;
    font-size: 21px; color: var(--ink);
  }
  .caption--front { left: 285px; }
  .caption--back { left: 716px; }

  .brand-dot {
    position: absolute; left: 50%; border-radius: 50%; background: var(--honey);
    transform: translateX(-50%);
  }
  .label--front .brand-dot { top: 82px; width: 90px; height: 90px; }
  .label--back .brand-dot { top: 452px; width: 56px; height: 56px; }

  .brand-name {
    position: absolute; left: 0; width: 100%; text-align: center;
    color: var(--honey); letter-spacing: 0.5px; white-space: nowrap;
  }
  .label--front .brand-name { top: 198px; font-size: 31px; }
  .label--back .brand-name { top: 518px; font-size: 19px; }

  .tagline {
    position: absolute; top: 284px; left: 0; width: 100%; text-align: center;
    font-family: "Gochi Hand", cursive; font-size: 19px; color: var(--honey);
    letter-spacing: 0.5px;
  }
  .product-name {
    position: absolute; top: 464px; left: 0; width: 100%; text-align: center;
    font-size: 21px; letter-spacing: -0.3px;
  }
  .product-size {
    position: absolute; top: 505px; left: 0; width: 100%; text-align: center;
    font-size: 10px; color: var(--muted);
  }
  .honeycomb-band {
    position: absolute; left: 0; bottom: 0; width: 100%; height: 120px;
    background: linear-gradient(to bottom, rgba(253,238,196,0) 0%, var(--honey-pale) 100%);
  }

  .section-title {
    position: absolute; left: 40px; font-size: 11px; color: var(--honey);
  }
  .section-title--ingredients { top: 40px; }
  .section-title--directions { top: 184px; }
  .ingredients-text {
    position: absolute; top: 54px; left: 40px; width: 326px;
    font-size: 8.3px; line-height: 10.3px; text-align: justify; color: var(--ink);
  }
  .note {
    position: absolute; left: 0; width: 100%; text-align: center; font-size: 9px;
  }
  .note--free { top: 127px; }
  .note--recycle { top: 327px; }

  .steps { position: absolute; top: 200px; left: 42px; width: 324px; list-style: none; }
  .step { position: relative; padding-left: 34px; font-size: 8.3px; line-height: 9.8px; text-align: justify; }
  .step + .step { margin-top: 8px; }
  .step__badge { position: absolute; left: 0; top: 2px; width: 27px; height: 28px; }
  .step__badge text { font-family: "Questrial", sans-serif; font-size: 16px; fill: var(--page); }

  .location {
    position: absolute; top: 569px; left: 0; width: 100%; text-align: center;
    font-size: 12px; color: var(--ink);
  }
</style>
</head>
<body>

<section class="label label--front">
  <div class="brand-dot"></div>
  <div class="brand-name">LINDEN MIST SKINCARE</div>
  <p class="tagline">Stay Gentle with Your Face</p>
  <h1 class="product-name">MOISTURIZING FACE CREAM</h1>
  <p class="product-size">120 ML</p>
  <div class="honeycomb-band" role="img" aria-label="Pale honey-yellow honeycomb pattern along the bottom edge"></div>
</section>

<section class="label label--back">
  <h2 class="section-title section-title--ingredients">INGREDIENTS</h2>
  <p class="ingredients-text">Raw fireweed honey, purified water, sweet almond oil, shea butter, jojoba seed oil, glycerin, aloe leaf juice, oat kernel extract, vitamin E, chamomile flower extract, calendula extract, beeswax, sunflower seed oil, rosehip oil, cocoa butter, lavender oil, green tea leaf extract, cucumber fruit extract, hyaluronic acid, squalane, xanthan gum, lactic acid, citric acid, rosemary leaf extract, evening primrose oil, argan kernel oil, vegetable glycerin, natural fragrance.</p>
  <p class="note note--free">Paraben and Sulfate Free</p>

  <h2 class="section-title section-title--directions">DIRECTION</h2>
  <ol class="steps">
    <li class="step">
      <svg class="step__badge" viewBox="0 0 27 28"><polygon points="13.5,0 27,7 27,21 13.5,28 0,21 0,7" fill="#f7be25"/><text x="13.5" y="21" text-anchor="middle">1</text></svg>
      Cleanse your face with warm water and gently pat the skin dry with a soft towel before applying the cream each morning.
    </li>
    <li class="step">
      <svg class="step__badge" viewBox="0 0 27 28"><polygon points="13.5,0 27,7 27,21 13.5,28 0,21 0,7" fill="#f7be25"/><text x="13.5" y="21" text-anchor="middle">2</text></svg>
      Warm a small amount between fingertips and smooth over face and neck using light upward circles.
    </li>
    <li class="step">
      <svg class="step__badge" viewBox="0 0 27 28"><polygon points="13.5,0 27,7 27,21 13.5,28 0,21 0,7" fill="#f7be25"/><text x="13.5" y="21" text-anchor="middle">3</text></svg>
      Use morning and night. Store in a cool, dry place away from direct sunlight.
    </li>
  </ol>
  <p class="note note--recycle">PLEASE RECYCLE</p>

  <div class="brand-dot"></div>
  <div class="brand-name">LINDEN MIST SKINCARE</div>
  <p class="location">Cedar Bay, BC</p>
</section>

<p class="caption caption--front">front</p>
<p class="caption caption--back">back</p>

</body>
</html>
```